Flyers

Modify Existing Flyer and create another for exterior company
Updates

Previous Brief has been updated- we want to update this existing one also

Target Market(s)

Exterior Remodeling Customers

Industry/Entity Type

Remodeling/Construction

```html
<!DOCTYPE html>
<html lang="en">
<head>
<meta charset="utf-8">
<title>Northline Remodeling Flyer</title>
<link href="https://fonts.googleapis.com/css2?family=Exo+2:wght@500;600;700&family=Mulish:wght@400;600;700;800&display=swap" rel="stylesheet">
<style>
  :root {
    --bg: #7a7a7a;
    --paper: #ffffff;
    --navy: #2b2f45;
    --navy-glass: rgba(43, 47, 69, 0.93);
    --orange: #ee5a24;
    --blue: #2a4fa8;
    --blue-bright: #2f6fcf;
    --ink: #2b2b2b;
    --text-blue: #2b4ba0;
  }
  * { box-sizing: border-box; margin: 0; padding: 0; }
  html, body { width: 1200px; height: 1200px; overflow: hidden; }
  body { background: var(--bg); position: relative; font-family: "Mulish", sans-serif; }

  .flyer {
    position: absolute; left: 156px; top: 30px;
    width: 888px; height: 1140px; background: var(--paper); overflow: hidden;
  }

  .hero-photo {
    position: absolute; left: 24px; top: 24px; width: 840px; height: 439px;
    background: linear-gradient(90deg, #eceae6 0%, #d9d5cf 18%, #3a7f70 34%, #2b6f61 60%, #2c6a5e 100%);
  }

  .headline-panel {
    position: absolute; left: 475px; top: 90px; width: 355px; height: 585px;
    background: var(--navy-glass); color: #fff;
  }
  .brand {
    position: absolute; top: 44px; left: 0; width: 100%; text-align: center;
    font-family: "Exo 2", sans-serif; font-weight: 600; color: var(--orange);
  }
  .brand-name { font-size: 44px; letter-spacing: 2px; line-height: 1; }
  .brand-tag { font-size: 15px; letter-spacing: 0.5px; margin-top: 10px; }

  .headline {
    position: absolute; left: 28px; top: 178px; width: 320px;
    font-family: "Exo 2", sans-serif; font-weight: 600;
  }
  .headline-lead { font-size: 47px; line-height: 1; color: #fff; letter-spacing: 0.5px; }
  .headline-main { font-size: 41px; line-height: 47px; color: var(--orange); margin-top: 12px; }
  .panel-rule { position: absolute; left: 28px; top: 445px; width: 67px; height: 2px; background: var(--blue-bright); }
  .panel-sub {
    position: absolute; left: 28px; top: 464px; width: 310px;
    font-size: 19px; line-height: 24px; font-weight: 600; text-transform: uppercase; color: #f2f2f2;
  }

  .photo { position: absolute; }
  .photo-bedroom { left: 475px; top: 684px; width: 171px; height: 145px;
    background: linear-gradient(180deg, #d9d4cb 0%, #c9c2b6 55%, #f1f0ee 75%, #8e7a66 100%); }
  .photo-porch { left: 657px; top: 684px; width: 172px; height: 145px;
    background: linear-gradient(180deg, #a8794e 0%, #b98a5e 22%, #6e9a4f 45%, #587f3e 70%, #5a3f2c 100%); }
  .photo-kitchen { left: 475px; top: 840px; width: 354px; height: 154px;
    background: linear-gradient(90deg, #f2f1ef 0%, #6b4028 14%, #7a4a2e 45%, #e9e7e4 70%, #6b4028 88%, #f0efec 100%); }

  .service { position: absolute; left: 0; width: 470px; }
  .service-head { display: flex; align-items: center; height: 30px; }
  .service-tab {
    width: 49px; height: 30px; background: linear-gradient(90deg, var(--blue) 0%, var(--blue-bright) 100%);
    display: flex; align-items: center; justify-content: flex-end; padding-right: 8px;
  }
  .service-title {
    margin-left: 8px; font-size: 17px; font-weight: 800; color: var(--orange); letter-spacing: 0.2px;
  }
  .service-intro {
    margin: 2px 0 0 57px; width: 405px; font-size: 12.3px; line-height: 15.3px; font-weight: 700; color: var(--text-blue);
  }
  .service-list { display: flex; margin: 12px 0 0 57px; }
  .service-list ul { list-style: none; width: 240px; }
  .service-list ul + ul { width: 170px; }
  .service-list li {
    position: relative; padding-left: 14px; font-size: 11.2px; line-height: 14px; margin-bottom: 3px; color: var(--ink);
  }
  .service-list li::before {
    content: ""; position: absolute; left: 0; top: 3px; width: 7px; height: 7px;
    background:
      linear-gradient(var(--orange), var(--orange)) 0 0 / 4px 7px no-repeat,
      linear-gradient(var(--orange), var(--orange)) 5px 0 / 2px 2px no-repeat;
  }

  .kitchen { top: 493px; }
  .bathroom { top: 678px; }
  .additions { top: 820px; }
  .decks { top: 981px; }

  .cta { position: absolute; right: 58px; top: 1018px; text-align: right; }
  .cta-lead { font-family: "Exo 2", sans-serif; font-weight: 500; font-size: 15.5px; color: #222; }
  .cta-lead span { color: var(--orange); }
  .cta-phone { font-family: "Mulish", sans-serif; font-weight: 800; font-size: 34px; line-height: 38px; color: var(--orange); }
  .cta-web { font-size: 12px; letter-spacing: 3px; color: #222; margin-top: 4px; font-weight: 600; }

  .footer-band {
    position: absolute; left: 59px; top: 1117px; width: 771px; height: 23px;
    background: linear-gradient(90deg, #2a45a6 0%, #2f78c8 50%, #2a45a6 100%);
  }
</style>
</head>
<body>
  <main class="flyer">
    <div class="hero-photo" role="img" aria-label="Bright bedroom with green wall, wooden headboard and white bedding"></div>

    <section class="headline-panel">
      <div class="brand">
        <div class="brand-name">NORTHLINE</div>
        <div class="brand-tag">ROOFING AND EXTERIORS</div>
      </div>
      <h1 class="headline">
        <div class="headline-lead">READY FOR</div>
        <div class="headline-main">A Beautiful and Functional Kitchen or Bathroom?</div>
      </h1>
      <div class="panel-rule"></div>
      <p class="panel-sub">Work with a top-rated local remodeling company in Millbrook Valley, IA</p>
    </section>

    <div class="photo photo-bedroom" role="img" aria-label="Remodeled bedroom with white bed and large window"></div>
    <div class="photo photo-porch" role="img" aria-label="Screened porch with wooden ceiling and dining set overlooking trees"></div>
    <div class="photo photo-kitchen" role="img" aria-label="Modern kitchen with walnut cabinets and marble island"></div>

    <section class="service kitchen">
      <div class="service-head">
        <div class="service-tab"><svg width="18" height="18" viewBox="0 0 18 18" fill="none" stroke="#fff" stroke-width="1.2"><rect x="2" y="7" width="14" height="9"/><line x1="2" y1="11" x2="16" y2="11"/><line x1="9" y1="7" x2="9" y2="16"/><circle cx="5" cy="4" r="1.5"/><circle cx="12" cy="4" r="1.5"/></svg></div>
        <h2 class="service-title">KITCHEN REMODELING</h2>
      </div>
      <p class="service-intro">Whatever your vision is for your new kitchen, our crew can help you bring it to life. You can trust us for:</p>
      <div class="service-list">
        <ul>
          <li>Open concept design services</li>
          <li>Kitchen cabinet installation services</li>
          <li>Kitchen countertop installation services</li>
          <li>Tile installation services</li>
          <li>Lighting installation services</li>
        </ul>
        <ul>
          <li>Plumbing upgrade services</li>
          <li>Electrical upgrade services</li>
          <li>Drywall services</li>
          <li>Painting services</li>
        </ul>
      </div>
    </section>

    <section class="service bathroom">
      <div class="service-head">
        <div class="service-tab"><svg width="18" height="18" viewBox="0 0 18 18" fill="none" stroke="#fff" stroke-width="1.2"><rect x="2" y="9" width="14" height="7"/><line x1="2" y1="12" x2="16" y2="12"/><circle cx="9" cy="5" r="3"/></svg></div>
        <h2 class="service-title">BATHROOM REMODELING</h2>
      </div>
      <p class="service-intro">When you hire us for your bathroom remodeling project, the possibilities are endless. Our experienced and talented team can:</p>
      <div class="service-list">
        <ul>
          <li>Install a custom tile shower</li>
          <li>Build a new vanity</li>
          <li>Install flooring and tile</li>
        </ul>
        <ul>
          <li>Replace your plumbing and light fixtures</li>
        </ul>
      </div>
    </section>

    <section class="service additions">
      <div class="service-head">
        <div class="service-tab"><svg width="18" height="18" viewBox="0 0 18 18" fill="none" stroke="#fff" stroke-width="1.2"><rect x="2" y="2" width="14" height="14"/><polyline points="2,14 6,14 6,10 10,10 10,6 14,6 14,2"/></svg></div>
        <h2 class="service-title">HOME ADDITIONS</h2>
      </div>
      <p class="service-intro">No matter what kind of space you need, our team will bring your vision to life. You can hire us if you need a:</p>
      <div class="service-list">
        <ul>
          <li>Bathroom addition</li>
          <li>Bedroom addition</li>
          <li>Garage addition</li>
          <li>Basement addition</li>
        </ul>
        <ul>
          <li>Guest room addition</li>
          <li>Living room addition</li>
          <li>Sunroom addition</li>
        </ul>
      </div>
    </section>

    <section class="service decks">
      <div class="service-head">
        <div class="service-tab"><svg width="18" height="18" viewBox="0 0 18 18" fill="none" stroke="#fff" stroke-width="1.2"><path d="M3 7 Q9 1 15 7 Z"/><line x1="9" y1="7" x2="9" y2="13"/><line x1="2" y1="13" x2="16" y2="13"/><line x1="3" y1="16" x2="15" y2="16"/></svg></div>
        <h2 class="service-title">DECKS/PATIOS</h2>
      </div>
      <p class="service-intro">An outdoor space is a great addition to any residential property. When you decide to build a patio or deck, you'll be able to experience a variety of benefits. Your outdoor area will increase your:</p>
      <div class="service-list">
        <ul>
          <li>Property value</li>
          <li>Curb appeal</li>
        </ul>
        <ul>
          <li>Functional living space</li>
        </ul>
      </div>
    </section>

    <div class="cta">
      <p class="cta-lead">CALL TODAY FOR YOUR <span>FREE ESTIMATE</span></p>
      <p class="cta-phone">555-014-2738</p>
      <p class="cta-web">www.northlineexteriors.com</p>
    </div>

    <div class="footer-band"></div>
  </main>
</body>
</html>
```